International oil and gas consultancy business needs a web design

Hello, I need a web design for a new oil and gas auditing consultancy business. My business undertakes contract audit assignments to review past costs of oil and gas operations (see attached Excel file for more details of the businesses services). I need the design to give the impression of a professional consultancy style of business, rather than a retail style of website. Note: this job is for LAYOUT DESIGN ONLY and not coding / development work.
The following are my key design principles:
1. BASIC DESIGN: I am after a simple and static web design. I don't want the pages busy or cluttered with too many images or detail.
2. HORIZONTAL TABS: I require a horizontal set of tabs towards the top of the screens (see Excel file) which remain in the same position on every page.
3. META TAG PLANNING: The design should allow for effective positioning of content so that key meta tag words can easily be built during the technical build stage.
4. NUMBER OF PAGES: The site will eventually have a maximum of 10 pages. Seven of the pages will reside under the tabs. Can you please present your opening submission for the first two page.
5. USE OF MY LOGO: The attached logo (JPEG file) should be used throughout the website. Please don't change the shape and colour.
6. COLOUR SCHEMES: Can you please consider any of the 3 colour schemes below:
A - dark red (to match the logo), light grey and perhaps another of your liking;
B - dark red (to match the logo), light cream and perhaps another of your liking;
C - dark red (to match the logo), white and perhaps another of your liking.
7. WORD CONTENT: I have attached an Excel file which shows the estimated word content for each page.
8. FUTURE USE OF DESIGN: I'm planning on building a Wordpress website. Can you please ensure the layout design supports this application.

Target Market(s)

oil and gas companies (small and large)

Industry/Entity Type

Oil And Gas

Font styles to use
Sans Serif

Requirements
Nice to have
• The KOR logo and business name should ideally be next to each other. Also, the logo and name should be part of the background graphics, not above it.

```html
<!DOCTYPE html>
<html lang="en">
<head>
<meta charset="utf-8">
<title>Keystone Oil Reviews</title>
<link href="https://fonts.googleapis.com/css2?family=Raleway:wght@300;400;500;600&family=Roboto+Condensed:wght@400;700&display=swap" rel="stylesheet">
<style>
:root{
  --red:#9b1b1e;
  --red-btn:#b3161b;
  --page:#ececec;
  --header:#f4f4f4;
  --nav:#4b4b4b;
  --nav-text:#f0f0f0;
  --ink:#222;
  --body-text:#666;
  --footer:#8c8c8c;
  --footer-text:#f2f2f2;
  --line:#b5b5b5;
}
*{margin:0;padding:0;box-sizing:border-box}
html,body{width:1200px;height:933px;overflow:hidden}
body{position:relative;background:var(--page);font-family:'Raleway',sans-serif;color:var(--ink)}
.site-header{position:absolute;left:172px;top:17px;width:847px;height:110px;background:var(--header);box-shadow:0 6px 6px -3px rgba(0,0,0,.25);border:1px solid #dcdcdc}
.brand{position:absolute;left:22px;top:30px;display:flex;align-items:center;gap:10px;color:var(--red);font-family:'Raleway',sans-serif;font-weight:600}
.brand-mark{font-size:34px;letter-spacing:1px}
.brand-name{font-size:15px;line-height:1.1;width:110px}
.main-nav{position:absolute;left:245px;top:34px;width:591px;height:38px;background:var(--nav);display:flex;align-items:center}
.main-nav a{font-family:'Roboto Condensed',sans-serif;font-size:11.5px;color:var(--nav-text);text-decoration:none;text-transform:uppercase;padding:0 17px;height:100%;display:flex;align-items:center;border-right:1px solid #3a3a3a;position:relative}
.main-nav a:last-child{border-right:none}
.main-nav a.active{color:#fff;font-weight:700}
.main-nav a.active::after{content:"";position:absolute;left:12px;right:12px;bottom:0;height:3px;background:var(--red-btn)}
.intro{position:absolute;top:160px;left:0;width:1200px;text-align:center}
.intro p{font-size:19px;font-weight:500;color:#1d1d1d}
.intro strong{display:block;margin-top:10px;font-size:22px;font-weight:500;color:var(--red)}
.hero{position:absolute;top:248px;left:0;width:1200px;height:350px}
.hero-photo{position:absolute;inset:0;background:linear-gradient(180deg,#9fbfdc 0%,#b9cfe2 45%,#6d8fb4 60%,#2b3f63 80%,#1c2c4b 100%)}
.hero-panel{position:absolute;left:281px;top:62px;width:449px;height:200px;background:rgba(255,255,255,.33)}
.hero-panel .lead{position:absolute;left:38px;top:18px;font-size:15px;font-weight:400;color:#333}
.service{position:absolute;left:36px;display:flex;align-items:center;font-size:25px;font-weight:400;color:#1d1d1d;white-space:nowrap}
.service svg{margin-right:10px}
.service em{font-style:normal;color:var(--red);margin-right:6px}
.more{margin-left:16px;background:var(--red-btn);color:#fff;font-size:10px;padding:3px 9px;border-radius:2px;font-family:'Roboto Condensed',sans-serif}
.about{position:absolute;top:634px;left:198px;width:810px;text-align:center;font-size:14px;line-height:21px;font-weight:400;color:var(--body-text)}
.site-footer{position:absolute;top:728px;left:0;width:1200px;height:205px;background:var(--footer);color:var(--footer-text)}
.col{position:absolute;top:19px}
.col h3{font-size:13px;font-weight:500;margin-bottom:10px}
.col p{font-size:11px;line-height:17px;color:#eee}
.col-nav{left:233px}
.col-nav ul{list-style:none}
.col-nav li{font-family:'Roboto Condensed',sans-serif;font-size:10px;text-transform:uppercase;line-height:18.5px}
.col-office{left:463px}
.col-postal{left:673px}
.contact-line{display:flex;align-items:center;gap:8px;font-size:11.5px;margin-top:17px}
.contact-line.email{color:#a31a1d;margin-top:11px}
.social{display:flex;gap:6px;margin-top:55px}
.social span{width:26px;height:23px;background:#555}
.col-news{left:829px}
.col-news h3{font-size:11px;margin-bottom:6px}
.field-row{display:flex;gap:3px}
.input{width:170px;height:20px;background:#a3a3a3;border:1px solid #b8b8b8}
.btn{background:var(--red-btn);color:#fff;font-size:10px;font-family:'Roboto Condensed',sans-serif;text-transform:uppercase;display:flex;align-items:center;justify-content:center}
.btn-go{width:26px;height:20px}
.question{font-size:11px;margin:13px 0 7px}
.textarea{width:199px;height:50px;background:#a3a3a3;border:1px solid #b8b8b8}
.btn-send{position:absolute;left:158px;top:128px;width:41px;height:17px}
.footer-base{position:absolute;left:233px;top:175px;width:795px;border-top:1px solid var(--line);display:flex;font-size:9px;color:#eee;padding-top:7px}
.footer-base span:nth-child(1){margin-left:184px}
.footer-base span:nth-child(2){margin-left:112px}
.footer-base span:nth-child(3){margin-left:128px}
</style>
</head>
<body>
<header class="site-header">
  <div class="brand"><span class="brand-mark">KOR</span><span class="brand-name">Keystone Oil Reviews</span></div>
  <nav class="main-nav">
    <a class="active" href="#">Home</a>
    <a href="#">About us</a>
    <a href="#">Services</a>
    <a href="#">Our partners</a>
    <a href="#">Approach</a>
    <a href="#">Whay choose us</a>
    <a href="#">Contact us</a>
  </nav>
</header>

<section class="intro">
  <p>We specialise in providing auditing services to the oil and gas industry.</p>
  <strong>THAT'S ALL WE DO!</strong>
</section>

<section class="hero">
  <div class="hero-photo" role="img" aria-label="Offshore oil platform at sea with an orange supply vessel under a clear sky"></div>
  <div class="hero-panel">
    <p class="lead">We are specialise in:</p>
    <div class="service" style="top:52px"><svg width="12" height="16" viewBox="0 0 12 16"><path d="M6 1C4 5 1.5 8 1.5 10.5a4.5 4.5 0 009 0C10.5 8 8 5 6 1z" fill="none" stroke="#333" stroke-width="1.3"/></svg><em>JOINT</em>VENTURE AUDITS<span class="more">MORE</span></div>
    <div class="service" style="top:100px"><svg width="12" height="16" viewBox="0 0 12 16"><path d="M6 1C4 5 1.5 8 1.5 10.5a4.5 4.5 0 009 0C10.5 8 8 5 6 1z" fill="none" stroke="#333" stroke-width="1.3"/></svg><em>CONTRACT</em>AUDITS<span class="more">MORE</span></div>
    <div class="service" style="top:148px"><svg width="12" height="16" viewBox="0 0 12 16"><path d="M6 1C4 5 1.5 8 1.5 10.5a4.5 4.5 0 009 0C10.5 8 8 5 6 1z" fill="none" stroke="#333" stroke-width="1.3"/></svg><em>OPERATIONS</em>AUDITS<span class="more">MORE</span></div>
  </div>
</section>

<p class="about">Keystone Oil Reviews is a Perth (Australia) based firm specialising in providing quality audit services for the oil and gasidustry. Our skills and knowledge of oil and gas, along with a deep understanding of business commercial needs, ensures the high quality of our services.</p>

<footer class="site-footer">
  <div class="col col-nav">
    <h3>Keystone Oil Reviews</h3>
    <ul><li>Home</li><li>About us</li><li>Services</li><li>Our partners</li><li>Approach</li><li>Whay choose us</li><li>Contact us</li></ul>
  </div>
  <div class="col col-office">
    <h3>Registered Office:</h3>
    <p>Unit 7, 18 Harbour Street<br>Fremantle WA 6160<br>Australia</p>
    <div class="contact-line"><svg width="13" height="13" viewBox="0 0 24 24"><path d="M6.6 10.8a15 15 0 006.6 6.6l2.2-2.2a1 1 0 011-.25 11.4 11.4 0 003.6.57 1 1 0 011 1V20a1 1 0 01-1 1A17 17 0 013 4a1 1 0 011-1h3.5a1 1 0 011 1c0 1.25.2 2.45.57 3.57a1 1 0 01-.25 1z" fill="#fff"/></svg>+61 (0)400 123 456</div>
    <div class="contact-line email"><svg width="14" height="10" viewBox="0 0 14 10"><rect x=".5" y=".5" width="13" height="9" fill="#a31a1d"/><path d="M.5 .5l6.5 5 6.5-5" fill="none" stroke="#e8b0b0"/></svg>admin@keystoneoilreviews.com</div>
  </div>
  <div class="col col-postal">
    <h3>Postal Address:</h3>
    <p>12 Wren Street<br>Claremont WA 6010<br>Australia</p>
    <div class="social"><span></span><span></span><span></span></div>
  </div>
  <div class="col col-news">
    <h3>For Newsletter enter your e-mail:</h3>
    <div class="field-row"><div class="input"></div><div class="btn btn-go">GO</div></div>
    <p class="question">Do you have a question?</p>
    <div class="textarea"></div>
    <div class="btn btn-send">SEND</div>
  </div>
  <div class="footer-base"><span>Copyright © 2014</span><span>Terms and Conditions</span><span>Privacy policy</span></div>
</footer>
</body>
</html>
```